Business Card Design Project

Professional business cards for law firm - a rough example of what we are looking for is attached. The logo, colour and styling of the name are all new and dont need to be changed. We need layout for front and back. We are looking for some imaginative layout of info. We are a young vibrant firm and not too conservative and are not adverse to something quite different.
Updates

Thank you for all the submissions.  We have been blown away with the quality of your work.  Our management team will be meeting later in the week to make our decision.  Again, thanks for the fabulous work.

Industry/Entity Type

Conservative

Requirements
Must have
• Logo and name as in attached example (colour and font)
Should not have
• Scales of Justice

```html
<!DOCTYPE html>
<html lang="en">
<head>
<meta charset="utf-8">
<title>Fairmont Reid Legal – Business Cards</title>
<link href="https://fonts.googleapis.com/css2?family=Mulish:wght@400;700;800&display=swap" rel="stylesheet">
<style>
  :root {
    --bg: #e9e7e3;
    --paper-top: #ffffff;
    --paper-bottom: #e4e5e6;
    --charcoal: #3a3a3d;
    --charcoal-deep: #2c2c2f;
    --green: #5e8a2e;
    --grey-text: #55575a;
    --ring: #6c6e71;
    --white: #ffffff;
    --light-text: #e6e6e6;
    --divider: #9a9a9d;
  }
  html, body {
    margin: 0;
    width: 1200px;
    height: 820px;
    overflow: hidden;
    background: var(--bg);
    font-family: "Mulish", sans-serif;
  }
  p { margin: 0; }
  .canvas {
    width: 1200px;
    height: 820px;
    display: flex;
    align-items: center;
    justify-content: center;
    gap: 40px;
  }
  .card {
    position: relative;
    width: 540px;
    height: 310px;
    border-radius: 18px;
    overflow: hidden;
    background: linear-gradient(160deg, var(--paper-top), var(--paper-bottom));
    box-shadow: 0 6px 18px rgba(0,0,0,.18);
  }
  .brand {
    position: absolute;
    display: flex;
    align-items: center;
    gap: 20px;
  }
  .brand-mark {
    flex: none;
    border-radius: 50%;
    border: 3px solid var(--ring);
    box-sizing: border-box;
  }
  .brand-name {
    color: var(--green);
    font-weight: 800;
    font-size: 26px;
    line-height: 1.1;
  }
  .tagline {
    margin-top: 6px;
    color: var(--grey-text);
    font-size: 12px;
    letter-spacing: .2px;
  }

  /* Back: practice areas */
  .card-back .brand { left: 40px; top: 24px; }
  .card-back .brand-mark { width: 112px; height: 112px; }
  .services {
    position: absolute;
    left: 40px;
    top: 148px;
    display: flex;
    gap: 70px;
  }
  .services ul { margin: 0; padding: 0; list-style: none; }
  .services li {
    color: var(--grey-text);
    font-size: 15px;
    line-height: 1.15;
  }
  .card-back .band {
    position: absolute;
    left: 0; right: 0; bottom: 0;
    height: 66px;
    background: linear-gradient(180deg, var(--charcoal), var(--charcoal-deep));
  }

  /* Front: contact */
  .card-front .brand { left: 70px; top: 40px; }
  .card-front .brand-mark { width: 112px; height: 112px; }
  .card-front .brand-name { font-size: 24px; }
  .stripe {
    position: absolute;
    left: 0; right: 0;
    top: 188px;
    height: 11px;
    background: var(--green);
  }
  .card-front .band {
    position: absolute;
    left: 0; right: 0;
    top: 199px; bottom: 0;
    background: linear-gradient(180deg, var(--charcoal), var(--charcoal-deep));
    display: flex;
    align-items: center;
    padding: 0 28px;
    color: var(--white);
  }
  .person { text-align: right; }
  .person-name {
    font-weight: 700;
    font-size: 19px;
  }
  .person-role {
    margin-top: 2px;
    font-size: 12px;
    color: #d9d9d9;
  }
  .divider {
    width: 1px;
    height: 68px;
    background: var(--divider);
    margin: 0 18px;
  }
  .contact {
    margin: 0;
    padding: 0;
    list-style: none;
    font-size: 11px;
    line-height: 1.45;
    color: var(--light-text);
  }
</style>
</head>
<body>
<main class="canvas">

  <section class="card card-back" aria-label="Business card back – practice areas">
    <div class="brand">
      <div class="brand-mark" aria-hidden="true"></div>
      <div>
        <p class="brand-name">Fairmont Reid Legal</p>
        <p class="tagline">clear counsel for every next step</p>
      </div>
    </div>
    <div class="services">
      <ul>
        <li>Family</li>
        <li>Restraining Orders</li>
        <li>Probate/Wills</li>
        <li>Dividing Fences</li>
      </ul>
      <ul>
        <li>Traffic</li>
        <li>Criminal</li>
        <li>Debt Recovery</li>
        <li>Financial Agreements</li>
      </ul>
    </div>
    <div class="band"></div>
  </section>

  <section class="card card-front" aria-label="Business card front – contact details">
    <div class="brand">
      <div class="brand-mark" aria-hidden="true"></div>
      <div>
        <p class="brand-name">Fairmont Reid Legal</p>
        <p class="tagline">clear counsel for every next step</p>
      </div>
    </div>
    <div class="stripe"></div>
    <div class="band">
      <div class="person">
        <p class="person-name">Clara Benning LLB BA</p>
        <p class="person-role">Solicitor</p>
      </div>
      <div class="divider"></div>
      <ul class="contact">
        <li>PO Box 512, Ashvale WA 6071</li>
        <li>T: 9400 1234, 6100 5678</li>
        <li>F: 6300 4411</li>
        <li>E: reception@fairmontreidlegal.com.au</li>
      </ul>
    </div>
  </section>

</main>
</body>
</html>
```